Used Car Dealer seeks an Amazing Business Card Design

We are looking for a business card design that incorporates our logo and grabs the attention of anyone we give the business card to.

Looking to use the same colors as the logo. Our Logo choice is the black background with Red and Silver/Grey Lettering.

We also would like to see some embossed designs.

Target Market(s)

Used Car Buyers, Automotive, Auto

Industry/Entity Type

Automotive

Contact Information for Business Card

BVEL7K
Gordon Whitlock
482 Tarrow Lane
Suite 207
Dunmore, GA 30412
Office (770) 555-0142
Cell (770) 555-0187
bvel7kga@quellmail.com
www.bvel7kga.com

Colors
ffffff
ee3036

Requirements
Must have
• Must include our logo (Black Background with Red and Silver/Grey Lettering)
Nice to have
• Embossed Design. Can be Single or Double Sided.

```html
<!DOCTYPE html>
<html lang="en">
<head>
<meta charset="utf-8">
<title>BVEL7K Business Card</title>
<link href="https://fonts.googleapis.com/css2?family=Arimo:wght@400;700&display=swap" rel="stylesheet">
<style>
  :root {
    --page-bg: #e6eaec;
    --card-white: #f3f4f5;
    --card-black: #1b1b1c;
    --card-black-light: #2e2e30;
    --accent-red: #ee3036;
    --accent-red-dark: #c5161c;
    --text-dark: #3a3a3a;
    --silver: #c9cbce;
  }
  * { margin: 0; padding: 0; box-sizing: border-box; }
  html, body { width: 1200px; height: 970px; overflow: hidden; }
  body {
    background: var(--page-bg);
    font-family: "Arimo", Arial, sans-serif;
    position: relative;
  }
  .business-card {
    position: absolute;
    left: 100px;
    top: 207px;
    width: 1000px;
    height: 556px;
    border-radius: 20px;
    overflow: hidden;
    box-shadow: 0 14px 40px rgba(0,0,0,0.25);
  }
  .card-shapes { position: absolute; inset: 0; }
  .holder-name {
    position: absolute;
    left: 66px;
    top: 120px;
    font-size: 30px;
    font-weight: 700;
    color: var(--accent-red);
    letter-spacing: 0.2px;
    white-space: nowrap;
  }
  .contact-list {
    position: absolute;
    left: 66px;
    top: 178px;
    list-style: none;
  }
  .contact-list li {
    display: flex;
    align-items: center;
    height: 32.5px;
    font-size: 24px;
    color: var(--text-dark);
    white-space: nowrap;
  }
  .contact-list svg { width: 24px; height: 24px; margin-right: 10px; flex: none; }
  .address {
    position: absolute;
    left: 66px;
    top: 330px;
    font-size: 24px;
    line-height: 32.5px;
    color: var(--text-dark);
    font-style: normal;
    white-space: nowrap;
  }
  .brand-name {
    position: absolute;
    left: 480px;
    right: 0;
    top: 268px;
    text-align: center;
    font-size: 64px;
    font-weight: 700;
    color: var(--silver);
    letter-spacing: 1px;
  }
</style>
</head>
<body>
  <section class="business-card">
    <svg class="card-shapes" viewBox="0 0 1000 556" preserveAspectRatio="none" aria-hidden="true">
      <defs>
        <linearGradient id="blackPanel" x1="0" y1="0" x2="1" y2="1">
          <stop offset="0" stop-color="#1b1b1c"/>
          <stop offset="0.55" stop-color="#2e2e30"/>
          <stop offset="1" stop-color="#1b1b1c"/>
        </linearGradient>
        <linearGradient id="redBand" x1="0" y1="0" x2="0" y2="1">
          <stop offset="0" stop-color="#c5161c"/>
          <stop offset="1" stop-color="#ee3036"/>
        </linearGradient>
      </defs>
      <rect width="1000" height="556" fill="url(#blackPanel)"/>
      <path d="M380 0 C480 120 490 380 250 556 L330 556 C520 400 500 130 405 0 Z" fill="url(#redBand)"/>
      <path d="M0 0 L380 0 C480 120 490 380 250 556 L0 556 Z" fill="var(--card-white)"/>
    </svg>

    <h1 class="holder-name">GORDON WHITLOCK</h1>

    <ul class="contact-list">
      <li>
        <svg viewBox="0 0 24 24"><rect x="6" y="2" width="12" height="20" rx="2.5" fill="none" stroke="var(--accent-red)" stroke-width="2.2"/><circle cx="12" cy="18" r="1.3" fill="var(--accent-red)"/></svg>
        (770) 555-0187
      </li>
      <li>
        <svg viewBox="0 0 24 24"><path d="M6.6 10.8a15 15 0 0 0 6.6 6.6l2.2-2.2c.3-.3.7-.4 1-.2 1.1.4 2.3.6 3.6.6.6 0 1 .4 1 1V20c0 .6-.4 1-1 1A17 17 0 0 1 3 4c0-.6.4-1 1-1h3.5c.6 0 1 .4 1 1 0 1.3.2 2.5.6 3.6.1.3 0 .7-.2 1z" fill="var(--accent-red)"/></svg>
        (770) 555-0142
      </li>
      <li>
        <svg viewBox="0 0 24 24"><rect x="2" y="5" width="20" height="14" fill="var(--accent-red)"/><path d="M2 5 L12 13 L22 5" fill="none" stroke="#fff" stroke-width="1.6"/></svg>
        bvel7kga@quellmail.com
      </li>
      <li>
        <svg viewBox="0 0 24 24" fill="none" stroke="var(--accent-red)" stroke-width="1.6"><circle cx="12" cy="12" r="9.5"/><ellipse cx="12" cy="12" rx="4" ry="9.5"/><path d="M2.5 12h19M4 7h16M4 17h16"/></svg>
        www.bvel7kga.com
      </li>
    </ul>

    <address class="address">
      482 Tarrow Lane<br>
      Suite 207<br>
      Dunmore, GA 30412
    </address>

    <div class="brand-name">BVEL7K</div>
  </section>
</body>
</html>
```